Business Card Ayurvedic Massage

I'm starting with my ayurvedic massage business and need a business card design. The design should be inline with my brand/logo as well as with the design of my website (www.lumo-thara.ch).
Front: logo and text "Ayurvedische Massagen"
back: name and adress (see details https://www.lumo-thara.ch/kontakt.html)

```html
<!DOCTYPE html>
<html lang="de">
<head>
<meta charset="utf-8">
<title>lumo-thara – Visitenkarte</title>
<link href="https://fonts.googleapis.com/css2?family=Lato:wght@400;700&display=swap" rel="stylesheet">
<style>
  :root {
    --bg: #e6e6e6;
    --maroon: #6d0c20;
    --white: #ffffff;
    --gold: #e0a526;
    --gold-deep: #b8731a;
    --text-light: #f7efe9;
  }
  html, body { margin: 0; padding: 0; overflow: hidden; }
  body { width: 1200px; height: 802px; background: var(--bg); font-family: "Lato", sans-serif; }
  .stage { position: relative; width: 1200px; height: 802px; }
  .card {
    position: absolute; top: 274px; width: 443px; height: 265px;
    background: var(--maroon);
    box-shadow: 2px 3px 6px rgba(0,0,0,0.35);
    overflow: hidden;
  }
  .card--contact { left: 136px; }
  .card--brand { left: 624px; }

  .side-strip { position: absolute; left: 0; top: 0; width: 132px; height: 100%; background: var(--white); }
  .illustration {
    position: absolute;
    background: radial-gradient(circle at 50% 50%, var(--gold) 0%, var(--gold-deep) 55%, rgba(184,115,26,0) 75%);
    opacity: 0.85;
  }
  .side-strip .illustration--top { left: 30px; top: 18px; width: 70px; height: 62px; }
  .side-strip .illustration--bottom { left: 30px; top: 186px; width: 70px; height: 62px; }
  .side-strip .wordmark {
    position: absolute; left: 73px; top: 133px;
    transform: translate(-50%, -50%) rotate(90deg);
    color: var(--gold-deep); font-size: 17px; font-weight: 400;
    letter-spacing: 0.5px; white-space: nowrap;
  }

  .contact { position: absolute; left: 175px; top: 66px; color: var(--text-light); }
  .contact__name { margin: 0; color: var(--gold); font-size: 16px; font-weight: 700; line-height: 1.1; }
  .contact__role { margin: 0 0 9px; font-size: 12.5px; line-height: 1.2; }
  .contact__list { list-style: none; margin: 0 0 6px 2px; padding: 0; font-size: 12.5px; line-height: 16px; }
  .contact__list li { display: flex; align-items: center; gap: 6px; }
  .contact__list svg { width: 10px; height: 10px; fill: var(--gold); flex: none; }
  .contact__address { margin: 0 0 0 2px; font-style: normal; font-size: 12.5px; line-height: 16px; }

  .card--brand .illustration--left { left: 82px; top: 86px; width: 76px; height: 94px; }
  .card--brand .illustration--right { left: 285px; top: 86px; width: 76px; height: 94px; }
  .card--brand .wordmark {
    position: absolute; left: 0; right: 0; top: 147px; text-align: center;
    color: var(--gold); font-size: 19px; font-weight: 400; letter-spacing: 0.5px;
    transform: translateY(-50%);
  }
</style>
</head>
<body>
<main class="stage">
  <section class="card card--contact">
    <div class="side-strip">
      <div class="illustration illustration--top" role="img" aria-label="Geschmückter Elefant mit Sonnenschirm"></div>
      <div class="wordmark">lumo-thara</div>
      <div class="illustration illustration--bottom" role="img" aria-label="Geschmückter Elefant mit Sonnenschirm"></div>
    </div>
    <div class="contact">
      <h1 class="contact__name">DANIEL BERGER</h1>
      <p class="contact__role">Managing Director</p>
      <ul class="contact__list">
        <li><svg viewBox="0 0 10 10"><path d="M1 3c0-1 1-2 4-2s4 1 4 2l-2 1-1-1H4L3 4zM2 5h6v4H2z"/></svg>+41 77 318 42 60</li>
        <li><svg viewBox="0 0 10 10"><path d="M0 2h10v6H0zM0 2l5 3.5L10 2v1L5 6.5 0 3z" fill-rule="evenodd"/></svg>info@lumo-thara.ch</li>
        <li><svg viewBox="0 0 10 10"><circle cx="5" cy="5" r="4.5"/><path d="M2 4h3v3H3zM6 2h2v2H6z" fill="#6d0c20"/></svg>www.lumo-thara.ch</li>
      </ul>
      <address class="contact__address">Lena Vogt, lumo-thara<br>Lindenweg 12<br>8867 Talmatt (SZ)</address>
    </div>
  </section>

  <section class="card card--brand">
    <div class="illustration illustration--left" role="img" aria-label="Geschmückter goldener Elefant mit Sonnenschirm"></div>
    <div class="wordmark">lumo-thara</div>
    <div class="illustration illustration--right" role="img" aria-label="Geschmückter goldener Elefant mit Sonnenschirm"></div>
  </section>
</main>
</body>
</html>
```